Dental X-Ray equipment company needs a 1 Full page ad creative for several industry magazines.

print ad where we show the docs an email template with the below questions like we were making the email for them to forward, we just write it on their behalf and offer it in the ad.  Come to www.quorvalradiant.com/email and download this template that you can forward to your sensor company…and we will send the answers from KELP Radiography to those questions for comparison.

You don’t have time for games.  Us neither.  (not sold on the wording, just that kind of direct headline)
That’s why we post our prices on our website.
We only offer one premium warranty plan/coverage with prices posted and what the coverage entails.
 
Not everyone who is adding or replacing a sensor will choose a TRIM sensor from KELP, we get that, but you deserve know the important financial details of a purchase this size.
 
Ask your sensor company to respond in writing/email:
How much is each sensor?
How much is each annual warranty plan you offer?
What is different about each plan?
What is the cost of replacing a non-working sensor under each plan offered?
What is the cost of replacing a sensor that is broken/damaged under each plan?
How many years can I keep this sensor under warranty? 
What’s the return policy if I am not happy?

One page ad
Size 1)

Trim Size - 8 x 10.5
Bleed Size - 8.25 x 10.75
Live Area - 7 x 10

Size 2)

Trim - 8 x 10.875
Bleed - 8.25 x 11.125
Live Area - 7 x 9.875

KELP Brand Hex #'s

Orange - ff6319
Teal - 56b1bf
Lt. Teal - aed9da
Blue: #38394B

Attaching some past creatives to get a feel for what we have done in the past.

Target Market(s)

Dentists

Requirements
Must have
• KELP Logo, pic of the sensor (called TRIM) and the TRIM logo.
Use the brand hex colors:
Orange - ff6319
Teal - 56b1bf
Lt. Teal - aed9da
Blue: #38394B

```html
<!DOCTYPE html>
<html lang="en">
<head>
<meta charset="utf-8">
<title>KELP Radiography – Sensor Pricing Ad</title>
<link rel="stylesheet" href="https://fonts.googleapis.com/css2?family=Cinzel:wght@400;500&family=Montserrat:wght@300;400;600;800&display=swap">
<style>
  :root {
    --navy: #28235f;
    --orange: #f26522;
    --white: #ffffff;
    --stage: #c8c8c8;
    --photo-light: #eeeeee;
    --photo-mid: #b9b9bd;
    --sensor-navy: #4c4d78;
  }
  * { box-sizing: border-box; margin: 0; padding: 0; }
  html, body {
    width: 1200px; height: 1026px; overflow: hidden;
    background: var(--stage);
  }
  .ad-page {
    position: absolute; left: 234px; top: 33px;
    width: 732px; height: 960px;
    background: var(--navy);
    overflow: hidden;
    font-family: "Montserrat", sans-serif;
    color: var(--white);
  }
  .brand-tab {
    position: absolute; top: 0; right: 0;
    width: 150px; height: 270px;
    background: var(--orange);
    border-bottom-left-radius: 26px;
    display: flex; align-items: center; justify-content: center;
    padding: 18px 0;
  }
  .brand-tab .brand-name {
    writing-mode: vertical-rl; transform: rotate(180deg);
    font-family: "Montserrat", sans-serif; font-weight: 800;
    font-size: 26px; line-height: 1.05; letter-spacing: 1px;
    color: var(--navy); text-transform: uppercase;
  }
  .headline {
    position: absolute; left: 60px; top: 120px; width: 500px;
    font-family: "Cinzel", serif; font-weight: 400;
    font-size: 40px; line-height: 1.12; letter-spacing: 1px;
  }
  .headline .accent { color: var(--orange); }
  .headline-rule {
    position: absolute; left: 60px; top: 232px;
    width: 470px; height: 1.5px; background: var(--white);
  }
  .subhead {
    position: absolute; left: 60px; top: 246px;
    font-weight: 300; font-size: 15px; letter-spacing: 0.5px;
  }
  .photo {
    position: absolute; border-radius: 50%;
    border: 6px solid var(--white);
  }
  .photo-hand {
    left: 90px; top: 318px; width: 446px; height: 446px;
    background: radial-gradient(circle at 55% 50%, var(--sensor-navy) 0 22%, var(--photo-light) 23% 60%, var(--photo-mid) 100%);
  }
  .photo-sensor {
    left: 370px; top: 270px; width: 230px; height: 230px;
    border-width: 0;
    background: radial-gradient(circle at 50% 45%, var(--sensor-navy) 0 34%, var(--white) 35%);
  }
  .offer-circle {
    position: absolute; left: 425px; top: 450px;
    width: 300px; height: 300px; border-radius: 50%;
    background: var(--orange); border: 5px solid var(--white);
    display: flex; align-items: center; justify-content: center;
    padding: 34px 40px;
  }
  .offer-circle p {
    font-size: 10.5px; line-height: 1.42; text-align: center;
  }
  .offer-circle strong { font-weight: 600; }
  .question-list {
    position: absolute; list-style: none;
    display: flex; flex-direction: column; gap: 14px;
  }
  .questions-left { left: 60px; top: 792px; width: 330px; }
  .questions-right { left: 420px; top: 776px; width: 290px; }
  .question-list li {
    display: flex; align-items: center; gap: 12px;
    font-size: 11px; line-height: 1.3;
  }
  .question-list .num {
    flex: none; width: 30px; height: 22px; border-radius: 11px;
    background: var(--orange); color: var(--white);
    font-weight: 800; font-size: 13px;
    display: flex; align-items: center; justify-content: center;
  }
  .product-tab {
    position: absolute; left: 430px; bottom: 0;
    width: 150px; height: 64px;
    background: var(--white);
    border-top-left-radius: 18px; border-top-right-radius: 18px;
    display: flex; align-items: center; justify-content: center;
  }
  .product-tab .product-name {
    font-weight: 800; font-size: 32px; letter-spacing: 2px;
    color: var(--navy);
  }
</style>
</head>
<body>
  <main class="ad-page">
    <div class="brand-tab"><span class="brand-name">KELP Radiography</span></div>

    <h1 class="headline">You <span class="accent">don’t</span> have <span class="accent">time</span><br>for <span class="accent">games</span>, us neither</h1>
    <div class="headline-rule"></div>
    <p class="subhead">THAT’S WHY WE POST OUR PRICES ON OUR WEBSITE</p>

    <div class="photo photo-hand" role="img" aria-label="Black and white photo of fingers holding a navy TRIM dental x-ray sensor"></div>
    <div class="photo photo-sensor" role="img" aria-label="Close-up of the navy TRIM sensor with its cable"></div>

    <div class="offer-circle">
      <p>Come to <strong>www.quorvalradiant.com/email</strong> and download this template that you can forward to your sensor company…and we will send the answers from KELP Radiography to those questions for comparison. We only offer one premium warranty plan/coverage with prices posted and what the coverage entails. Not everyone who is adding or replacing a sensor will choose a TRIM sensor from KELP, we get that, but you deserve know the important financial details of a purchase this size.</p>
    </div>

    <ol class="question-list questions-left">
      <li><span class="num">1</span>Ask your sensor company to respond in writing/email</li>
      <li><span class="num">2</span>How much is each annual warranty plan you offer?</li>
      <li><span class="num">3</span>What is the cost of replacing a non-working sensor under each plan offered?</li>
      <li><span class="num">4</span>What is different about each plan?</li>
    </ol>
    <ol class="question-list questions-right">
      <li><span class="num">5</span>What is the cost of replacing a sensor that is broken/damaged under each plan?</li>
      <li><span class="num">6</span>How many years can I keep this sensor under warranty?</li>
      <li><span class="num">7</span>What’s the return policy if I am not happy?</li>
    </ol>

    <div class="product-tab"><span class="product-name">TRIM</span></div>
  </main>
</body>
</html>
```